Health software company called BRIGHT MERIDIAN, committed to innovation and technological excellence

The powerpoint presentation template is necessary, very necessary is elegant and modern with innovative images and the color palette attached. The presentation will be used for the business plan and investor presentations that we will use to raise funds. Please, recommend a modern typeface, as well as format to be able to use it and incorporate it as part of the company's brand guidelines. Great diversity of technological solutions
Updates

Very low attendance of designers for a high budget. Very few proposals and no capture my interest

Need extra days to review

Need extra days to review

Need extra days to review

Target Market(s)

managers, managers of public and private health centers, government states, investors

Industry/Entity Type

It Company

Font styles to use
Serif

Requirements
Must have
• The powerpoint presentation template is necessary, very necessary is elegant, minimalist and modern with innovative images and the color palette attached. it must be refined in demarcated style
Nice to have
• very nice, visually harmonic avoid saturation
Should not have
• NO dark colors NO dark colors NO dark colors NO dark colors NO dark colors

```html
<!DOCTYPE html>
<html lang="en">
<head>
<meta charset="utf-8">
<title>Bright Meridian — Presentation Template</title>
<link href="https://fonts.googleapis.com/css2?family=Questrial&family=Poppins:wght@600&family=Nunito+Sans:wght@400;600;700&display=swap" rel="stylesheet">
<style>
:root{
  --blue:#1e88f0;
  --blue-mid:#5aa9f5;
  --blue-soft:#9cc8f7;
  --blue-pale:#dcebfc;
  --blue-wash:#eef5fe;
  --teal:#3ee0b2;
  --grey:#8b9099;
  --line:#e2ecf8;
  --white:#ffffff;
  --deck-a:#2f74dc;
  --deck-b:#5d9eee;
  --tile-orange:#f3a530;
  --tile-red:#e4513f;
  --tile-blue:#3a9be0;
  --tile-green:#8cc63f;
  --suit:#50607c;
  --skin-bg:#eef1f5;
}
html,body{margin:0;padding:0;overflow:hidden;background:var(--white);}
.canvas{position:relative;width:1200px;height:2426px;overflow:hidden;background:var(--white);font-family:"Nunito Sans",sans-serif;}
.slide{position:absolute;width:501px;height:282px;background:var(--white);box-shadow:0 2px 7px rgba(40,60,90,.28);overflow:hidden;}
.slide > *{position:absolute;margin:0;}
.col-l{left:85px}.col-r{left:613px}
.row-1{top:19px}.row-2{top:315px}.row-3{top:613px}.row-4{top:910px}
.row-5{top:1206px}.row-6{top:1501px}.row-7{top:1797px}.row-8{top:2093px}
.slide.deck{background:linear-gradient(135deg,var(--deck-a),var(--deck-b));}
.title-square{left:26px;top:20px;width:9px;height:9px;background:var(--blue);}
.brand-name{right:12px;bottom:9px;font-family:"Nunito Sans",sans-serif;font-weight:700;font-size:6px;letter-spacing:.6px;color:var(--blue);text-transform:uppercase;}
.title{left:42px;top:14px;font-family:"Poppins",sans-serif;font-weight:600;font-size:14px;line-height:20px;color:var(--blue);}
.title.light{color:var(--white);}
.txt{font-size:6.3px;line-height:1.5;color:var(--grey);}
.txt.blue{color:var(--blue);}
.txt.white{color:var(--white);}
.txt p{margin:0 0 5px;}
.bullets{padding:0 0 0 8px;list-style:disc;}
.bullets li{margin-bottom:5px;}
.screen{background:linear-gradient(135deg,var(--tile-orange) 0%,var(--tile-red) 32%,var(--tile-blue) 64%,var(--tile-green) 100%);}
.office{background:linear-gradient(160deg,#eaf1f8 0%,#c9d8e9 55%,#7f93b3 100%);}
.portrait{border:1px solid var(--blue-soft);background:linear-gradient(180deg,var(--skin-bg) 0%,#d9dfe7 55%,var(--suit) 100%);}
.name{font-family:"Poppins",sans-serif;font-weight:600;font-size:7px;color:var(--blue);text-align:center;}
.role{font-size:5.5px;color:var(--grey);text-align:center;}
.socials{display:flex;gap:3px;}
.socials span{width:9px;height:9px;background:var(--blue);display:block;}
.socials span:nth-child(2){background:var(--blue-mid);}
.socials span:nth-child(3){background:var(--blue-soft);}
.icon{width:16px;height:16px;}
.tbl{border-collapse:collapse;font-size:5.6px;}
.tbl th{background:var(--blue);color:var(--white);height:18px;width:36px;font-weight:400;line-height:1.1;border-left:1px solid rgba(255,255,255,.35);}
.tbl td{height:16px;text-align:center;color:var(--grey);border-bottom:1px solid var(--line);}
.tbl .lab{background:var(--blue);color:var(--white);text-align:left;padding-left:12px;border-bottom:1px solid rgba(255,255,255,.35);border-left:none;}
.year{font-family:"Questrial",sans-serif;font-size:7px;color:var(--blue);}
.agenda-item{font-size:7.5px;color:var(--blue);display:flex;align-items:center;gap:8px;}
.agenda-item::before{content:"";width:6px;height:6px;background:var(--blue);display:block;margin-left:-3px;}
</style>
</head>
<body>
<main class="canvas">

  <section class="slide col-l row-1">
    <div class="title-square"></div>
    <h2 class="title">Lorem ipsum dolor sit amet</h2>
    <div class="txt" style="left:42px;top:38px;width:430px">Bright Meridian builds connected health software that links clinics, teams and patient records in one secure place, so care leaders make faster and clearer decisions every single day across every site.</div>
    <ul class="txt bullets" style="left:30px;top:140px;width:95px">
      <li>Secure records for every clinic we serve.</li>
      <li>Real-time data shared across teams.</li>
      <li>Cloud tools built around care.</li>
      <li>Clear reports for health leaders.</li>
    </ul>
    <div class="screen" role="img" aria-label="Desktop monitor showing a tiled health dashboard" style="left:140px;top:92px;width:218px;height:178px;border-radius:4px"></div>
    <div class="txt" style="left:376px;top:118px;width:112px">Our platform brings scheduling, billing and clinical insight together, so managers see the full picture, plan staff with ease and act with confidence when it matters most.</div>
    <div class="brand-name">Bright Meridian</div>
  </section>

  <section class="slide col-r row-1">
    <div class="title-square"></div>
    <h2 class="title">Lorem ipsum dolor</h2>
    <svg class="icon" style="left:32px;top:98px" viewBox="0 0 16 16"><rect x="2" y="9" width="2" height="5" fill="#1e88f0"/><rect x="6" y="6" width="2" height="8" fill="#1e88f0"/><rect x="10" y="3" width="2" height="11" fill="#1e88f0"/><rect x="1" y="14" width="13" height="1" fill="#1e88f0"/></svg>
    <div class="txt" style="left:60px;top:96px;width:110px">Live dashboards track outcomes and costs for each site in one view.</div>
    <svg class="icon" style="left:32px;top:136px" viewBox="0 0 16 16"><circle cx="8" cy="8" r="6" fill="none" stroke="#1e88f0" stroke-width="1.4"/><ellipse cx="8" cy="8" rx="2.6" ry="6" fill="none" stroke="#1e88f0" stroke-width="1.2"/><line x1="2" y1="8" x2="14" y2="8" stroke="#1e88f0" stroke-width="1.2"/></svg>
    <div class="txt" style="left:60px;top:134px;width:110px">Cloud access lets teams work from any clinic, city or state network.</div>
    <svg class="icon" style="left:32px;top:174px" viewBox="0 0 16 16"><path d="M2 6h10l-3-3M14 10H4l3 3" fill="none" stroke="#1e88f0" stroke-width="1.5"/></svg>
    <div class="txt" style="left:60px;top:172px;width:110px">Smooth data exchange connects labs, wards and billing in seconds.</div>
    <div class="txt blue" style="left:30px;top:205px;width:190px;font-size:7px">Trusted by public and private health centres that need reliable, modern tools to serve their patients better.</div>
    <div class="screen" role="img" aria-label="Hand holding a white tablet showing a tiled health dashboard" style="left:278px;top:53px;width:134px;height:229px;border-radius:10px 10px 0 0;opacity:.9"></div>
    <div class="brand-name">Bright Meridian</div>
  </section>

  <section class="slide col-l row-2">
    <div class="title-square"></div>
    <h2 class="title">Lorem ipsum dolor sit amet</h2>
    <div class="txt blue" style="left:30px;top:60px;width:135px;text-align:right">
      <p>Patient journeys become simple when every record, visit and result lives in one calm and secure space that staff can trust and open in seconds.</p>
      <p>Our mobile tools keep doctors and nurses informed at the bedside, on rounds and between sites, without extra steps.</p>
    </div>
    <div class="screen" role="img" aria-label="Black tablet showing a tiled health dashboard" style="left:206px;top:93px;width:88px;height:145px;border-radius:7px"></div>
    <div class="txt" style="left:312px;top:108px;width:115px">
      <p>Clear layouts guide each user to the next task, reducing errors and saving time.</p>
      <p>Built-in alerts flag urgent cases early for the care team.</p>
      <p>Every update syncs across devices instantly and safely.</p>
    </div>
    <div class="brand-name">Bright Meridian</div>
  </section>

  <section class="slide col-r row-2">
    <div class="title-square"></div>
    <h2 class="title">Lorem ipsum dolor</h2>
    <div class="screen" role="img" aria-label="Monitor, tablet and phone showing the same health dashboard" style="left:22px;top:55px;width:270px;height:198px;border-radius:4px"></div>
    <div style="left:318px;top:56px;width:168px;font-family:'Questrial',sans-serif;font-size:11px;line-height:1.25;color:var(--blue-mid)">Lorem ipsum dolor sit amet consectetuer adipiscing elit.</div>
    <div class="txt" style="left:318px;top:92px;width:165px">
      <p>One platform for every screen: desktop, tablet and phone share the same clear design and the same secure data, so teams move freely between devices during the day.</p>
      <p>Managers review results in the office, doctors update notes on rounds and staff confirm visits on the go, all in real time.</p>
    </div>
    <div class="brand-name">Bright Meridian</div>
  </section>

  <section class="slide col-l row-3">
    <div class="title-square"></div>
    <h2 class="title">The Team</h2>
    <div class="portrait" role="img" aria-label="Portrait of a team member in a suit" style="left:80px;top:80px;width:52px;height:52px"></div>
    <div class="name" style="left:66px;top:140px;width:80px">Lorem Ipsum</div>
    <div class="role" style="left:66px;top:151px;width:80px">Chief Executive</div>
    <div class="txt" style="left:70px;top:164px;width:72px;text-align:center">Leads strategy and growth across all health partners.</div>
    <div class="socials" style="left:89px;top:220px"><span></span><span></span><span></span></div>

    <div class="portrait" role="img" aria-label="Portrait of a team member" style="left:176px;top:80px;width:52px;height:52px"></div>
    <div class="name" style="left:162px;top:140px;width:80px">Lorem Ipsum</div>
    <div class="role" style="left:162px;top:151px;width:80px">Product Lead</div>
    <div class="txt" style="left:166px;top:164px;width:72px;text-align:center">Shapes tools around the daily needs of care teams.</div>
    <div class="socials" style="left:185px;top:220px"><span></span><span></span><span></span></div>

    <div class="portrait" role="img" aria-label="Portrait of a team member in a suit" style="left:272px;top:80px;width:52px;height:52px"></div>
    <div class="name" style="left:258px;top:140px;width:80px">Lorem Ipsum</div>
    <div class="role" style="left:258px;top:151px;width:80px">Head of Engineering</div>
    <div class="txt" style="left:262px;top:164px;width:72px;text-align:center">Builds secure systems that scale with every clinic.</div>
    <div class="socials" style="left:281px;top:220px"><span></span><span></span><span></span></div>

    <div class="portrait" role="img" aria-label="Portrait of a team member" style="left:368px;top:80px;width:52px;height:52px"></div>
    <div class="name" style="left:354px;top:140px;width:80px">Lorem Ipsum</div>
    <div class="role" style="left:354px;top:151px;width:80px">Clinical Advisor</div>
    <div class="txt" style="left:358px;top:164px;width:72px;text-align:center">Brings hospital insight to every product decision.</div>
    <div class="socials" style="left:377px;top:220px"><span></span><span></span><span></span></div>
    <div class="brand-name">Bright Meridian</div>
  </section>

  <section class="slide col-r row-3">
    <div style="left:174px;top:0;width:150px;height:282px;background:var(--blue-wash)"></div>
    <div class="title-square"></div>
    <h2 class="title">Meet the Team</h2>
    <div class="portrait" role="img" aria-label="Portrait of a team member" style="left:51px;top:67px;width:72px;height:72px"></div>
    <div class="name" style="left:47px;top:145px;width:80px">Lorem Ipsum</div>
    <div class="role" style="left:47px;top:156px;width:80px">Chief Executive</div>
    <div style="left:30px;top:192px;width:10px;height:10px;background:var(--blue)"></div>
    <div class="txt" style="left:46px;top:193px;width:110px">@brightmeridian.ceo</div>
    <div style="left:30px;top:210px;width:10px;height:10px;background:var(--blue-mid)"></div>
    <div class="txt" style="left:46px;top:211px;width:110px">/brightmeridian.team</div>
    <div style="left:30px;top:228px;width:10px;height:10px;background:var(--blue)"></div>
    <div class="txt" style="left:46px;top:229px;width:110px">in/brightmeridian-lead</div>
    <div style="left:186px;top:46px;font-family:'Questrial',sans-serif;font-size:8px;color:var(--blue)">AT VERO EOS ET ACCUSAM</div>
    <div class="txt" style="left:186px;top:60px;width:128px">
      <p>Over fifteen years of experience guiding digital change in public and private hospitals across the region, with a focus on safe and simple patient data.</p>
      <p>Founded the company to give care managers modern tools that feel calm, clear and reliable every day of the week.</p>
      <p>Speaks often on health innovation and leads our work with investors and state partners.</p>
    </div>
    <div style="left:379px;top:44px;width:1px;height:178px;background:var(--blue-soft)"></div>
    <div class="year" style="left:352px;top:42px">2017</div>
    <div class="year" style="left:352px;top:82px">2016</div>
    <div class="year" style="left:352px;top:122px">2015</div>
    <div class="year" style="left:352px;top:167px">2014</div>
    <div class="year" style="left:352px;top:207px">2013</div>
    <div style="left:376px;top:45px;width:7px;height:7px;background:var(--blue)"></div>
    <div style="left:376px;top:85px;width:7px;height:7px;background:var(--blue)"></div>
    <div style="left:376px;top:125px;width:7px;height:7px;background:var(--blue)"></div>
    <div style="left:376px;top:170px;width:7px;height:7px;background:var(--blue)"></div>
    <div style="left:376px;top:210px;width:7px;height:7px;background:var(--blue)"></div>
    <div class="txt" style="left:392px;top:42px;width:92px">Series A round closed with new health investors.</div>
    <div class="txt" style="left:392px;top:82px;width:92px">Platform launched in forty public clinics.</div>
    <div class="txt" style="left:392px;top:122px;width:92px">First mobile tools for ward staff.</div>
    <div class="txt" style="left:392px;top:167px;width:92px">Partnership with two regional hospital groups.</div>
    <div class="txt" style="left:392px;top:207px;width:92px">Company founded by a small team of engineers.</div>
    <div class="brand-name">Bright Meridian</div>
  </section>

  <section class="slide deck col-l row-4">
    <div role="img" aria-label="Two business people shaking hands, tinted blue" style="left:0;top:0;width:501px;height:282px;background:linear-gradient(120deg,#2563c9 0%,#4a8ae0 45%,#7fb0ee 70%,#3f7fd8 100%)"></div>
    <h2 class="title light" style="left:0;top:22px;width:501px;text-align:center;font-size:12px">Our Awesome Clients</h2>
    <div class="portrait" role="img" aria-label="Portrait of a client" style="left:48px;top:138px;width:72px;height:72px;border-color:#fff"></div>
    <div class="txt white" style="left:48px;top:215px;width:72px;text-align:center;font-size:7px">Lorem Ipsum</div>
    <div class="portrait" role="img" aria-label="Portrait of a client" style="left:160px;top:138px;width:72px;height:72px;border-color:#fff"></div>
    <div class="txt white" style="left:160px;top:215px;width:72px;text-align:center;font-size:7px">Lorem Ipsum</div>
    <div class="portrait" role="img" aria-label="Portrait of a client" style="left:272px;top:138px;width:72px;height:72px;border-color:#fff"></div>
    <div class="txt white" style="left:272px;top:215px;width:72px;text-align:center;font-size:7px">Lorem Ipsum</div>
    <div class="portrait" role="img" aria-label="Portrait of a client" style="left:384px;top:138px;width:72px;height:72px;border-color:#fff"></div>
    <div class="txt white" style="left:384px;top:215px;width:72px;text-align:center;font-size:7px">Lorem Ipsum</div>
  </section>

  <section class="slide col-r row-4">
    <div class="title-square"></div>
    <h2 class="title">Our Awesome Partners</h2>
    <div style="left:30px;top:84px;width:440px;height:1px;background:var(--blue-soft)"></div>
    <div class="txt blue" style="left:15px;top:68px;width:100px;text-align:center">Lorem ipsum dolor sit amet</div>
    <div class="txt blue" style="left:136px;top:68px;width:100px;text-align:center">Lorem ipsum dolor sit amet</div>
    <div class="txt blue" style="left:258px;top:68px;width:100px;text-align:center">Lorem ipsum dolor sit amet</div>
    <div class="txt blue" style="left:380px;top:68px;width:100px;text-align:center">Lorem ipsum dolor sit amet</div>
    <div style="left:61px;top:81px;width:7px;height:7px;background:var(--blue)"></div>
    <div style="left:182px;top:81px;width:7px;height:7px;background:var(--blue)"></div>
    <div style="left:304px;top:81px;width:7px;height:7px;background:var(--blue)"></div>
    <div style="left:426px;top:81px;width:7px;height:7px;background:var(--blue)"></div>
    <div class="office" role="img" aria-label="Partner at an office desk" style="left:15px;top:122px;width:100px;height:60px"></div>
    <div class="office" role="img" aria-label="Partner with a headset at a computer" style="left:136px;top:122px;width:100px;height:60px"></div>
    <div class="office" role="img" aria-label="Partner working in an office" style="left:258px;top:122px;width:100px;height:60px"></div>
    <div class="office" role="img" aria-label="Partner standing in a bright office" style="left:380px;top:122px;width:100px;height:60px"></div>
    <div class="txt" style="left:15px;top:190px;width:100px">Regional hospital group using our records suite in all wards since launch.</div>
    <div class="txt" style="left:136px;top:190px;width:100px">Patient support centre running our scheduling and call tools daily.</div>
    <div class="txt" style="left:258px;top:190px;width:100px">State health office sharing secure data through our network.</div>
    <div class="txt" style="left:380px;top:190px;width:100px">Private clinic chain tracking outcomes with our reports.</div>
    <div class="brand-name">Bright Meridian</div>
  </section>

  <section class="slide deck col-l row-5">
    <div role="img" aria-label="People reviewing charts at a desk, tinted blue" style="left:0;top:0;width:501px;height:282px;background:linear-gradient(120deg,#8dbbf0 0%,#4d8fe2 40%,#2f6fd4 70%,#5c9be8 100%)"></div>
    <div style="left:250px;top:24px;width:218px;text-align:right;font-family:'Questrial',sans-serif;font-size:21px;line-height:1.15;color:var(--white)">Clients Data<br>and Profit</div>
    <svg style="left:132px;top:36px" width="160" height="206" viewBox="0 0 160 206">
      <g fill="#3ee0b2">
        <rect x="10" y="154" width="11" height="40"/><rect x="28" y="132" width="11" height="62"/>
        <rect x="46" y="89" width="11" height="105"/><rect x="64" y="52" width="11" height="142"/>
        <rect x="82" y="84" width="11" height="110"/><rect x="100" y="109" width="11" height="85"/>
        <rect x="118" y="112" width="11" height="82"/><rect x="136" y="84" width="11" height="110"/>
      </g>
      <g fill="#ffffff" font-family="Nunito Sans, sans-serif" font-size="6" text-anchor="middle">
        <text x="15.5" y="150">17</text><text x="33.5" y="128">26</text><text x="51.5" y="85">45</text><text x="69.5" y="48">62</text>
        <text x="87.5" y="80">48</text><text x="105.5" y="105">37</text><text x="123.5" y="108">36</text><text x="141.5" y="80">48</text>
      </g>
      <g fill="#ffffff" opacity=".8" font-family="Nunito Sans, sans-serif" font-size="4.5" text-anchor="middle">
        <text x="15.5" y="202">Jan</text><text x="33.5" y="202">Feb</text><text x="51.5" y="202">Mar</text><text x="69.5" y="202">Apr</text>
        <text x="87.5" y="202">May</text><text x="105.5" y="202">Jun</text><text x="123.5" y="202">Jul</text><text x="141.5" y="202">Aug</text>
      </g>
    </svg>
    <div class="txt white" style="left:52px;top:184px;width:80px;font-size:7px">Lorem ipsum dolor</div>
    <div class="txt white" style="left:30px;top:196px;width:96px">Monthly revenue from new clinic contracts grew steadily all year.</div>
  </section>

  <section class="slide deck col-r row-5">
    <div role="img" aria-label="Hand pointing at growth charts, tinted blue" style="left:0;top:0;width:502px;height:282px;background:linear-gradient(120deg,#2a66d0 0%,#4d8fe2 50%,#2f6fd4 80%,#6ea5ee 100%)"></div>
    <h2 class="title light" style="left:0;top:16px;width:502px;text-align:center;font-size:12px">Clients Data and Profit</h2>
    <div class="txt white" style="left:30px;top:40px;width:442px;text-align:center">Bright Meridian clients report shorter waiting times, fewer billing errors and stronger returns within the first year, while staff spend less time on paperwork and more time with patients in every department we support.</div>
    <svg style="left:81px;top:136px" width="100" height="100" viewBox="0 0 100 100">
      <circle cx="50" cy="50" r="40" fill="none" stroke="rgba(255,255,255,.25)" stroke-width="9"/>
      <circle cx="50" cy="50" r="40" fill="none" stroke="#3ee0b2" stroke-width="9" stroke-dasharray="193.5 251.3" transform="rotate(-90 50 50)"/>
      <text x="50" y="40" fill="#fff" font-family="Nunito Sans, sans-serif" font-size="6" text-anchor="middle">Text</text>
      <text x="50" y="58" fill="#3ee0b2" font-family="Questrial, sans-serif" font-size="18" text-anchor="middle">77%</text>
    </svg>
    <div class="txt white" style="left:190px;top:160px;width:80px">Clinics that cut patient waiting times.</div>
    <svg style="left:305px;top:136px" width="100" height="100" viewBox="0 0 100 100">
      <circle cx="50" cy="50" r="40" fill="none" stroke="rgba(255,255,255,.25)" stroke-width="9"/>
      <circle cx="50" cy="50" r="40" fill="none" stroke="#3ee0b2" stroke-width="9" stroke-dasharray="163.4 251.3" transform="rotate(-90 50 50)"/>
      <text x="50" y="40" fill="#fff" font-family="Nunito Sans, sans-serif" font-size="6" text-anchor="middle">Text</text>
      <text x="50" y="58" fill="#3ee0b2" font-family="Questrial, sans-serif" font-size="18" text-anchor="middle">65%</text>
    </svg>
    <div class="txt white" style="left:412px;top:160px;width:80px">Growth in yearly client profit.</div>
  </section>

  <section class="slide col-l row-6">
    <div class="title-square"></div>
    <h2 class="title">Our Customers Say</h2>
    <div style="left:96px;top:62px;width:252px;text-align:center;font-size:7.2px;line-height:1.5;color:var(--grey)">“Lorem ipsum dolor sit amet, consetetur sadipscing elitr, sed diam nonumy eirmod tempor invidunt ut labore et dolore magna aliquyam erat, sed diam voluptua. At vero eos et accusam et justo duo dolores et ea rebum.”</div>
    <div style="left:356px;top:112px;width:12px;height:12px;background:var(--blue-soft)"></div>
    <div style="left:368px;top:100px;width:10px;height:10px;background:#cfe3fb"></div>
    <div style="left:372px;top:124px;width:16px;height:16px;background:var(--blue-mid)"></div>
    <div class="portrait" role="img" aria-label="Portrait of a smiling customer" style="left:400px;top:61px;width:66px;height:86px;border:none"></div>
    <div style="left:88px;top:170px;width:12px;height:12px;background:var(--blue-soft)"></div>
    <div style="left:102px;top:157px;width:26px;height:26px;background:var(--blue)"></div>
    <div style="left:96px;top:190px;width:8px;height:8px;background:var(--blue-mid)"></div>
    <div class="txt" style="left:48px;top:210px;width:82px">A calm, clear system our whole team uses every day.</div>
    <div style="left:134px;top:154px;width:82px;height:81px;background:var(--blue-pale)"></div>
    <div class="portrait" role="img" aria-label="Portrait of a customer" style="left:224px;top:154px;width:75px;height:81px;border:none"></div>
    <div style="left:307px;top:154px;width:82px;height:81px;background:var(--blue)"></div>
    <div class="txt white" style="left:315px;top:182px;width:66px;text-align:center">Faster care and happier staff in every clinic we run.</div>
    <div style="left:392px;top:154px;width:82px;height:81px;background:var(--blue-pale)"></div>
    <div class="brand-name">Bright Meridian</div>
  </section>

  <section class="slide col-r row-6">
    <div class="title-square"></div>
    <h2 class="title">Our Sales</h2>
    <div class="txt" style="left:42px;top:38px;width:440px">Sales grew across every region as more public and private health centres moved their daily work onto our platform, with renewals staying high and new contracts signed each quarter.</div>
    <table class="tbl" style="left:0;top:96px">
      <tr><th class="lab" style="width:127px"></th><th>Lorem Ipsum</th><th>Lorem Ipsum</th><th>Lorem Ipsum</th><th>Lorem Ipsum</th></tr>
      <tr><td class="lab">Lorem ipsum dolor sit</td><td>11</td><td>12</td><td>13</td><td>14</td></tr>
      <tr><td class="lab">Lorem ipsum dolor sit</td><td>21</td><td>22</td><td>23</td><td>24</td></tr>
      <tr><td class="lab">Lorem ipsum dolor sit</td><td>31</td><td>32</td><td>33</td><td>34</td></tr>
      <tr><td class="lab">Lorem ipsum dolor sit</td><td>41</td><td>42</td><td>43</td><td>44</td></tr>
      <tr><td class="lab">Lorem ipsum dolor sit</td><td>5</td><td>6</td><td>7</td><td>8</td></tr>
    </table>
    <ul class="txt bullets" style="left:305px;top:96px;width:180px">
      <li>Public clinic contracts rose in each quarter, led by new state partners.</li>
      <li>Private hospital groups renewed at a strong rate and added new wards.</li>
      <li>Mobile tools became our fastest growing product line this year.</li>
      <li>Average contract value increased as clients adopted more modules.</li>
    </ul>
    <div class="brand-name">Bright Meridian</div>
  </section>

  <section class="slide col-l row-7">
    <div class="title-square"></div>
    <h2 class="title">Our Profits</h2>
    <div class="txt" style="left:42px;top:38px;width:440px">Profit margins improved as our cloud platform scaled, keeping costs low while adding value for every client, partner and investor who joined us on the journey so far.</div>
    <ul class="txt bullets" style="left:30px;top:100px;width:170px">
      <li>Recurring income now makes up most of yearly revenue.</li>
      <li>Hosting costs per clinic fell as the network grew.</li>
      <li>Support requests dropped thanks to clearer tools.</li>
      <li>New modules lifted profit per client each year.</li>
    </ul>
    <table class="tbl" style="left:222px;top:104px">
      <tr><th class="lab" style="width:85px"></th><th>Lorem Ipsum</th><th>Lorem Ipsum</th><th>Lorem Ipsum</th><th>Lorem Ipsum</th></tr>
      <tr><td class="lab">Lorem ipsum dolor sit</td><td>11</td><td>12</td><td>13</td><td>14</td></tr>
      <tr><td class="lab">Lorem ipsum dolor sit</td><td>21</td><td>22</td><td>23</td><td>24</td></tr>
      <tr><td class="lab">Lorem ipsum dolor sit</td><td>31</td><td>32</td><td>33</td><td>34</td></tr>
      <tr><td class="lab">Lorem ipsum dolor sit</td><td>41</td><td>42</td><td>43</td><td>44</td></tr>
      <tr><td class="lab">Lorem ipsum dolor sit</td><td>5</td><td>6</td><td>7</td><td>8</td></tr>
    </table>
    <div class="brand-name">Bright Meridian</div>
  </section>

  <section class="slide col-r row-7">
    <div class="title-square"></div>
    <h2 class="title">Our Profits</h2>
    <div class="txt" style="left:24px;top:68px;width:108px">Quarterly profit rose sharply after launch, then held steady as we invested in new tools for public health centres and expanded our teams to meet rising demand.</div>
    <svg style="left:155px;top:62px" width="290" height="190" viewBox="0 0 290 190">
      <text x="14" y="8" fill="#1e88f0" font-family="Nunito Sans, sans-serif" font-size="6">Lorem Ipsum</text>
      <g stroke="#e2ecf8" stroke-width="1">
        <line x1="14" y1="30" x2="280" y2="30"/><line x1="14" y1="60" x2="280" y2="60"/>
        <line x1="14" y1="90" x2="280" y2="90"/><line x1="14" y1="120" x2="280" y2="120"/>
        <line x1="14" y1="150" x2="280" y2="150"/>
      </g>
      <line x1="14" y1="14" x2="14" y2="172" stroke="#c9d6e6"/>
      <line x1="14" y1="172" x2="280" y2="172" stroke="#c9d6e6"/>
      <g fill="#8b9099" font-family="Nunito Sans, sans-serif" font-size="4.5" text-anchor="end">
        <text x="10" y="32">50</text><text x="10" y="62">40</text><text x="10" y="92">30</text><text x="10" y="122">20</text><text x="10" y="152">10</text>
      </g>
      <polyline fill="none" stroke="#5aa9f5" stroke-width="1.4" points="24,150 46,132 68,95 90,68 112,86 134,90 156,93 178,110 200,100 222,122 244,96 266,92"/>
      <g fill="#1e88f0">
        <circle cx="24" cy="150" r="2"/><circle cx="46" cy="132" r="2"/><circle cx="68" cy="95" r="2"/><circle cx="90" cy="68" r="2"/>
        <circle cx="112" cy="86" r="2"/><circle cx="134" cy="90" r="2"/><circle cx="156" cy="93" r="2"/><circle cx="178" cy="110" r="2"/>
        <circle cx="200" cy="100" r="2"/><circle cx="222" cy="122" r="2"/><circle cx="244" cy="96" r="2"/><circle cx="266" cy="92" r="2"/>
      </g>
      <g fill="#8b9099" font-family="Nunito Sans, sans-serif" font-size="4.5" text-anchor="middle">
        <text x="24" y="181">Text</text><text x="46" y="181">Text</text><text x="68" y="181">Text</text><text x="90" y="181">Text</text>
        <text x="112" y="181">Text</text><text x="134" y="181">Text</text><text x="156" y="181">Text</text><text x="178" y="181">Text</text>
        <text x="200" y="181">Text</text><text x="222" y="181">Text</text><text x="244" y="181">Text</text><text x="266" y="181">Text</text>
      </g>
    </svg>
    <div class="brand-name">Bright Meridian</div>
  </section>

  <section class="slide col-l row-8">
    <div class="title-square"></div>
    <h2 class="title">Our 2018 Agenda</h2>
    <div style="left:203px;top:0;width:1px;height:282px;background:var(--blue-soft)"></div>
    <div class="agenda-item" style="left:203px;top:80px">Lorem Ipsum Dolor Sit Amet</div>
    <div class="agenda-item" style="left:203px;top:110px">Lorem Ipsum Dolor Sit Amet</div>
    <div class="agenda-item" style="left:203px;top:139px">Lorem Ipsum Dolor Sit Amet</div>
    <div class="agenda-item" style="left:203px;top:168px">Lorem Ipsum Dolor Sit Amet</div>
    <div class="agenda-item" style="left:203px;top:198px">Lorem Ipsum Dolor Sit Amet</div>
    <div class="agenda-item" style="left:203px;top:227px">Lorem Ipsum Dolor Sit Amet</div>
    <div class="brand-name">Bright Meridian</div>
  </section>

  <section class="slide deck col-r row-8">
    <div role="img" aria-label="City office buildings, tinted blue" style="left:0;top:0;width:502px;height:282px;background:linear-gradient(135deg,#5c9be8 0%,#79aef0 50%,#4a88e0 100%)"></div>
    <div role="img" aria-label="Smiling businessman in a suit with arms folded" style="left:332px;top:0;width:170px;height:282px;background:linear-gradient(180deg,#8fbcf2 0%,#d7e4f3 30%,#3f6fb8 70%,#2f5fae 100%)"></div>
    <div class="txt white" style="left:30px;top:38px;width:160px;font-size:7.5px">Bright Meridian</div>
    <div class="txt white" style="left:30px;top:50px;width:160px">
      +1 555 014 2290<br>
      hello@brightmeridian.co<br>
      www.brightmeridian.co<br>
      120 Harbor Lane, Suite 4<br>
      Riverton, NV 89000
    </div>
    <div style="left:30px;top:140px;font-family:'Questrial',sans-serif;font-size:15px;letter-spacing:.5px;color:var(--white)">LOREM IPSUM DOLOR</div>
    <div class="txt white" style="left:30px;top:162px;width:290px">Thank you for your time. We would be glad to share our full plan, meet your team and show how our platform can support health centres in your region.</div>
    <div class="socials" style="left:30px;top:230px;gap:8px">
      <span style="width:14px;height:14px;background:rgba(255,255,255,.85)"></span>
      <span style="width:14px;height:14px;background:rgba(255,255,255,.85)"></span>
      <span style="width:14px;height:14px;background:rgba(255,255,255,.85)"></span>
      <span style="width:14px;height:14px;background:rgba(255,255,255,.85)"></span>
    </div>
  </section>

</main>
</body>
</html>
```